Dr Mira Thalen, Orthopaedic Hand Surgeon

I am an orthopaedic hand surgeon and need business cards that reflect the surgery I do. I operate on bones, ligaments, tendons, and soft tissues. I can do microsurgery (surgery under an operating microscope) - including connecting ends of cut nerves and arteries in the fingers together. As an orthopaedic surgeon, I also fix fractures and manage orthopaedic trauma in the rest of the body. I favour black as a colour, and have some pictures of hand X-rays that you can use in the design, if you think that would look good (feel free to crop).
Updates

Hi all. Thank you for all your submissions so far. Please note that I have updated my project brief. I would like to emphasise that use of the logos that I have provided is optional, and if used, I would very much prefer the logo not to dominate the card, but add to the overall aesthetic of the card. Warm regards, Mira

Target Market(s)

Referring medical practitioners, hand therapists, patients

Industry/Entity Type

Healthcare

Contact Information for Business Card

Dr Mira Thalen
Orthopaedic Hand Surgeon
MBBS BSc (Med), MIntPH (Merit), FCWES (Ortho), FUPelV

Font styles to use
Serif

Colors

Designer to choose colors to be used in the design.

Requirements
Must have
• Space for:
• 2 addresses (a PO Box Address and a consulting suite address) - to be confirmed
• 1 phone number - to be confirmed
Nice to have
• Please choose one of the FCWES logos (I included 3 - colour, black reverse, and greyscale); if you include this in the design, IT SHOULD NOT DOMINATE THE CARD, but be smaller and more discreet.
• I have also attached the FUPelV logo (colour and greyscale); if you choose to include this in the design, IT SHOULD NOT DOMINATE THE CARD, but be smaller and more discreet.
• I would love to be able to update details on the card as time goes on, and thus would like to own the template for the card as well.
• Also I would love discussion with regard to any changes on the card, if I am not completely happy with the design, and would like to discuss things such as ease of printing, finish on the cards (matte, polish) etc.
Should not have
• I don't like the card to look too crowded

```html
<!DOCTYPE html>
<html lang="en">
<head>
<meta charset="utf-8">
<title>Dr Mira Thalen – Business Card</title>
<link rel="stylesheet" href="https://fonts.googleapis.com/css2?family=Roboto:wght@300;400;500;700&display=swap">
<style>
  :root {
    --backdrop: #e9e7e3;
    --card: #ffffff;
    --blue: #1e6a92;
    --blue-dark: #155677;
    --red: #e0303c;
    --grey: #6f6f6f;
    --ink: #4a4a4a;
  }
  html, body {
    margin: 0;
    width: 1200px;
    height: 1023px;
    overflow: hidden;
    background: var(--backdrop);
    font-family: "Roboto", Arial, sans-serif;
  }
  .card {
    position: absolute;
    left: 75px;
    top: 211px;
    width: 1050px;
    height: 600px;
    background: linear-gradient(160deg, #ffffff 0%, #f3f3f3 100%);
    border-radius: 16px;
    overflow: hidden;
    box-shadow: 0 12px 30px rgba(0,0,0,0.18);
  }
  .college {
    position: absolute;
    left: 64px;
    top: 66px;
    display: flex;
    align-items: center;
    gap: 22px;
  }
  .college__mark {
    width: 70px;
    height: 70px;
    background: var(--blue);
  }
  .college__name {
    font-size: 64px;
    font-weight: 400;
    color: var(--blue);
    letter-spacing: 1px;
    line-height: 1;
  }
  .college__caption {
    font-size: 17px;
    color: var(--ink);
    line-height: 1.35;
    margin-left: 4px;
  }
  .doctor {
    position: absolute;
    right: 64px;
    top: 62px;
    text-align: right;
  }
  .doctor__name {
    font-size: 44px;
    font-weight: 700;
    color: var(--blue);
    margin: 0 0 8px;
  }
  .doctor__role,
  .doctor__credentials {
    font-size: 24px;
    font-weight: 300;
    color: var(--red);
    line-height: 1.35;
    margin: 0;
  }
  .divider {
    position: absolute;
    left: 64px;
    right: 64px;
    top: 330px;
    height: 2px;
    background: var(--blue);
  }
  .contact {
    position: absolute;
    left: 64px;
    top: 356px;
    list-style: none;
    margin: 0;
    padding: 0;
    font-size: 23px;
    font-weight: 300;
    color: var(--grey);
  }
  .contact li {
    display: flex;
    align-items: center;
    gap: 14px;
    line-height: 40px;
  }
  .contact svg { width: 18px; height: 18px; }
  .address {
    position: absolute;
    right: 64px;
    top: 360px;
    text-align: right;
    font-size: 23px;
    font-weight: 300;
    color: var(--grey);
    line-height: 1.5;
    margin: 0;
    font-style: normal;
  }
  .edge-band {
    position: absolute;
    left: 0;
    bottom: 0;
    width: 1050px;
    height: 80px;
  }
</style>
</head>
<body>
  <section class="card" aria-label="Business card of Dr Mira Thalen">
    <div class="college">
      <div class="college__mark" aria-hidden="true"></div>
      <div>
        <div class="college__name">FCWES</div>
        <div class="college__caption">Fellow of the<br>Coastal &amp; Western Surgical College</div>
      </div>
    </div>

    <header class="doctor">
      <h1 class="doctor__name">Dr Mira Thalen</h1>
      <p class="doctor__role">Orthopaedic Hand Surgeon</p>
      <p class="doctor__credentials">MBBS BSc (Med), MIntPH<br>(Merit), FCWES (Ortho), FUPelV</p>
    </header>

    <div class="divider"></div>

    <ul class="contact">
      <li>
        <svg viewBox="0 0 24 24" aria-hidden="true"><path fill="#1e6a92" d="M6.6 10.8a15 15 0 0 0 6.6 6.6l2.2-2.2c.3-.3.7-.4 1-.2 1.1.4 2.3.6 3.6.6.6 0 1 .4 1 1V20c0 .6-.4 1-1 1A17 17 0 0 1 3 4c0-.6.4-1 1-1h3.5c.6 0 1 .4 1 1 0 1.3.2 2.5.6 3.6.1.3 0 .7-.2 1z"/></svg>
        555 018 0370
      </li>
      <li>
        <svg viewBox="0 0 24 24" aria-hidden="true"><rect x="3" y="5" width="18" height="14" rx="1.5" fill="none" stroke="#1e6a92" stroke-width="2"/><path d="M3 6l9 7 9-7" fill="none" stroke="#1e6a92" stroke-width="2"/></svg>
        info@thalenhand.com
      </li>
      <li>
        <svg viewBox="0 0 24 24" aria-hidden="true"><circle cx="12" cy="12" r="9" fill="none" stroke="#1e6a92" stroke-width="2"/><path d="M3 12h18M12 3c3 3 3 15 0 18M12 3c-3 3-3 15 0 18" fill="none" stroke="#1e6a92" stroke-width="1.6"/></svg>
        www.thalenhand.com
      </li>
    </ul>

    <address class="address">1480 Alder Ridge<br>Lane Brookfield, TX 70412</address>

    <svg class="edge-band" viewBox="0 0 1050 80" preserveAspectRatio="none" aria-hidden="true">
      <path d="M0 44 H640 C680 44 690 26 730 26 H1050 V32 H730 C694 32 684 50 640 50 H0 Z" fill="var(--red)"/>
      <path d="M0 58 H640 C680 58 692 36 736 36 H1050 V80 H0 Z" fill="var(--blue)"/>
    </svg>
  </section>
</body>
</html>
```